SEO Company Needs a Professional, Bold Business Card Design

Kelvo SEO
2487 N Harlow Ave #315
Brenton, TX 78599
512-555-0184
http://www.kelvoseo-demo.com
Kelvo SEO is an internet marketing company specializing in SEO for higher-end businesses. We are looking for a professional and bold (edgy) design that communicates our forward thinking SEO strategies. Our typical client is a small to medium US business that has never had SEO work done on their website but does has active marketing. We want our business card design to instill confidence in our services through a professional and bold look. We we would also like the design elements to be in line with the services we offer - ranking client websites in the search engine results, namely Zarnix.
Design Specifics:
Card design should have square edges.
Design should be delivered in fully layered and editable PSD file. Designing in AI is fine but I need a PSD file in case we have any changes in contact information or need additional cards for employees.
The design should compliment the attached logo.
Company Name:
Kelvo SEO
Address:
2487 N Harlow Ave #315
Brenton, TX 78599
Personal Info:
Dorian Welk
Owner
owner@kelvoseo-demo.com
Phone:
877-555-0139 (KELVO UP)
Website:
http://www.kelvoseo-demo.com
Slogan:
Could Your Website Be Generating More Business?
Target Market(s)
High-end business owners - doctors, lawyers, specialists, business owners doing 250k in profit.
Industry/Entity Type
Internet
Contact Information for Business Card
Company Name:
Kelvo SEO
Address:
482 Larkfield Rd Ste 210
Brenton, TX 78599
Personal Info:
Dorian Welk
Owner
owner@kelvoseo-demo.com
Phone:
877-555-0139 (KELVO UP)
Website:
www.kelvoseo-demo.com
Slogan:
Requirements
Must have
- Card design should have square edges.
- Background should be WHITE only.
- Design should be delivered in fully layered and editable PSD file. Designing in AI is fine but I need a PSD file in case we have any changes in contact information or need additional cards for employees.

```html
<!DOCTYPE html>
<html lang="en">
<head>
<meta charset="utf-8">
<title>Kelvo SEO – Business Card</title>
<link rel="stylesheet" href="https://fonts.googleapis.com/css2?family=Open+Sans:wght@600;700&display=swap">
<style>
  :root {
    --backdrop: #d1d2d4;
    --paper: #ffffff;
    --navy: #0d2d50;
    --red: #ed1f24;
    --sky: #27a8e0;
  }
  html, body {
    margin: 0;
    padding: 0;
    width: 1200px;
    height: 1200px;
    overflow: hidden;
    background: var(--backdrop);
    font-family: "Open Sans", Arial, sans-serif;
  }
  .canvas { position: relative; width: 1200px; height: 1200px; }
  .card {
    position: absolute;
    top: 321px;
    width: 559px;
    height: 558px;
    background: var(--paper);
    overflow: hidden;
  }
  .card--front { left: 26px; }
  .card--back { left: 615px; }

  .band { position: absolute; left: 0; width: 100%; }
  .band--top-navy { top: 0; height: 29px; background: var(--navy); }
  .band--top-red { top: 0; height: 29px; background: var(--red); }
  .band--bottom-red { bottom: 0; height: 30px; background: var(--red); }

  .brand {
    position: absolute;
    left: 0;
    width: 100%;
    display: flex;
    justify-content: center;
    align-items: center;
    gap: 16px;
    color: var(--navy);
    font-weight: 700;
    font-size: 62px;
    letter-spacing: -1px;
    line-height: 1;
  }
  .brand__dot {
    width: 54px; height: 54px;
    border-radius: 50%;
    background: var(--navy);
  }
  .card--front .brand { top: 118px; }
  .card--back .brand { top: 250px; }

  .address-strip {
    position: absolute;
    top: 268px;
    left: 0;
    width: 100%;
    height: 86px;
    box-sizing: border-box;
    border-top: 6px solid var(--navy);
    border-bottom: 6px solid var(--navy);
    background: var(--red);
    display: flex;
    flex-direction: column;
    justify-content: center;
    align-items: center;
    color: var(--sky);
    font-weight: 700;
    font-size: 18px;
    line-height: 22px;
  }

  .contact-list {
    position: absolute;
    top: 392px;
    left: 20px;
    margin: 0;
    padding: 0;
    list-style: none;
  }
  .contact-list li {
    display: flex;
    align-items: center;
    gap: 11px;
    height: 26px;
    color: var(--red);
    font-weight: 700;
    font-size: 18px;
  }
  .contact-list svg { width: 16px; height: 16px; flex: none; }

  .person {
    position: absolute;
    top: 392px;
    right: 21px;
    text-align: right;
  }
  .person__name {
    margin: 0;
    color: var(--red);
    font-weight: 700;
    font-size: 31px;
    line-height: 1.15;
  }
  .person__role {
    margin: 0;
    color: var(--sky);
    font-weight: 700;
    font-size: 17px;
    line-height: 1.1;
  }

  .peaks { position: absolute; left: 0; bottom: 0; width: 559px; height: 120px; }
</style>
</head>
<body>
<div class="canvas">

  <section class="card card--front">
    <div class="band band--top-navy"></div>

    <div class="brand"><span class="brand__dot"></span>Kelvo SEO</div>

    <div class="address-strip">
      <span>482 Larkfield Rd Ste 210</span>
      <span>Brenton, TX 78599</span>
    </div>

    <ul class="contact-list">
      <li>
        <svg viewBox="0 0 16 16"><rect width="16" height="16" fill="#27a8e0"/><path d="M4.5 3.5h2l1 2.5-1.3 1a6 6 0 0 0 2.8 2.8l1-1.3 2.5 1v2a1 1 0 0 1-1 1A8.5 8.5 0 0 1 3.5 4.5a1 1 0 0 1 1-1z" fill="#fff"/></svg>
        877-555-0139
      </li>
      <li>
        <svg viewBox="0 0 16 16"><rect width="16" height="16" fill="#27a8e0"/><g fill="none" stroke="#fff" stroke-width="1"><circle cx="8" cy="8" r="5"/><ellipse cx="8" cy="8" rx="2.2" ry="5"/><path d="M3 8h10M4 5.5h8M4 10.5h8"/></g></svg>
        www.kelvoseo-demo.com
      </li>
      <li>
        <svg viewBox="0 0 16 16"><rect width="16" height="16" fill="#27a8e0"/><g fill="none" stroke="#fff" stroke-width="1.2"><rect x="3" y="4.5" width="10" height="7"/><path d="M3 4.5l5 4 5-4"/></g></svg>
        owner@kelvoseo-demo.com
      </li>
    </ul>

    <div class="person">
      <p class="person__name">Dorian Welk</p>
      <p class="person__role">Owner</p>
    </div>

    <svg class="peaks" viewBox="0 0 559 120" aria-hidden="true">
      <polygon points="0,72 71,58 186,120 0,120" fill="#0d2d50"/>
      <polygon points="186,120 311,57 426,120" fill="#27a8e0"/>
      <polygon points="426,120 559,18 559,120" fill="#0d2d50"/>
      <polyline points="0,70 71,56 186,120" fill="none" stroke="#ed1f24" stroke-width="3"/>
      <polyline points="186,120 311,56 426,120" fill="none" stroke="#ed1f24" stroke-width="2"/>
      <polyline points="426,120 559,14" fill="none" stroke="#ed1f24" stroke-width="3"/>
    </svg>
  </section>

  <section class="card card--back">
    <div class="band band--top-red"></div>
    <div class="brand"><span class="brand__dot"></span>Kelvo SEO</div>
    <div class="band band--bottom-red"></div>
  </section>

</div>
</body>
</html>
```